Zielgruppe
Ich bin Schriftsteller und meine Zielgruppe sind hauptsächlich (nicht nur) weibliche Leser.
Hallo liebe Designer,
ich benötige das Cover sowohl als ebook-cover als auch als Cover für ein gedrucktes Taschenbuch.
Folgendes soll auf dem Cover stehen:
Autor: Heike Sommerlund
Titel: Die Hütte im Moor
Als kleiner 'Untertitel' soll 'Holding on' stehen und irgendwo unten 'Roman'.
Folgendes ist der Inhalt meines Buches:
An einem heißen Sommertag lernt die schüchterne Miriam den Schriftsteller Jonas Treuholt kennen. Nach und nach befreit er sie aus ihrem inneren Gefängnis. Ihr Glück scheint perfekt, bis ein Skandal über Jonas hereinbricht, der das Potential hat, nicht nur ihrer beider Liebe, sondern auch ihr Leben zu zerstören.
Schon bald müssen sie erkennen, dass sie es mit einem Feind zu tun haben, dessen Verbindungen nicht nur in höchste Kreise reichen, sondern dessen Köpfe auch nachwachsen, sollte man einen abschlagen.
Eine aufregende Mischung aus Liebesgeschichte, Politthriller und Medienkritik.
Wenn Sie mehr Informationen zum Inhalt bzw. der Stimmung des Romans benötigen, fragen Sie bitte jederzeit.
Für das Cover habe ich folgende Ideen/Vorschläge:
Wenn es mehr in eine realistische Richtung geht, stelle ich mir einen kleinen verwunschen Steg vor. Es soll idyllisch/verwunschen wirken.
Hier ein paar Bilder, die ich schön finde:
https://www.pixelvorrat.example/de/bild/steg-see-waldufer-7730419826
oder diese Art
https://www.pixelvorrat.example/de/bild/see-landschaft-ufer-6621845093
https://www.pixelvorrat.example/de/bild/holzsteg-ruhiger-see-5849107732
https://www.pixelvorrat.example/de/bild/enten-auf-holzbruecke-teich-3907264158
Wenn Sie Bilder mit einem kleinen Zelt finden, wäre es schön, wenn es auch einen Platz auf dem Cover finden könnte. Das Zelt klein, so das gerade so zwei Personen reinpassen. Es muss auch nicht ganz zu sehen sein, ein Stüc..

```html
<!DOCTYPE html>
<html lang="de">
<head>
<meta charset="utf-8">
<title>Die Hütte im Moor – Heike Sommerlund</title>
<link rel="stylesheet" href="https://fonts.googleapis.com/css2?family=Cinzel:wght@400;700&family=Montserrat:wght@600&display=swap">
<style>
  :root {
    --backdrop: #ece8e3;
    --navy: #173a6b;
    --accent: #e0552b;
    --white: #ffffff;
  }
  html, body {
    margin: 0;
    padding: 0;
    width: 925px;
    height: 1200px;
    overflow: hidden;
    background: var(--backdrop);
  }
  .cover {
    position: absolute;
    left: 110px;
    top: 40px;
    width: 704px;
    height: 1120px;
    overflow: hidden;
  }
  .cover-photo {
    position: absolute;
    inset: 0;
    width: 100%;
    height: 100%;
  }
  .title-glow {
    position: absolute;
    left: 50%;
    top: 230px;
    width: 760px;
    height: 620px;
    transform: translate(-50%, -50%);
    background: radial-gradient(ellipse at center, rgba(255,255,255,0.95) 0%, rgba(255,255,255,0.8) 45%, rgba(255,255,255,0) 72%);
  }
  .author, .title, .subtitle {
    position: absolute;
    left: 0;
    width: 100%;
    margin: 0;
    text-align: center;
    font-family: "Cinzel", serif;
    color: var(--navy);
  }
  .author {
    top: 84px;
    font-size: 42px;
    font-weight: 700;
    line-height: 1;
    letter-spacing: 1px;
  }
  .title {
    top: 188px;
    font-size: 112px;
    font-weight: 700;
    line-height: 132px;
    letter-spacing: -1px;
  }
  .title span { display: block; }
  .subtitle {
    top: 470px;
    font-size: 54px;
    font-weight: 400;
    line-height: 1;
    color: var(--accent);
  }
  .genre-tab {
    position: absolute;
    left: 228px;
    bottom: 0;
    width: 248px;
    height: 78px;
    background: var(--navy);
    border-radius: 12px 12px 0 0;
    display: flex;
    align-items: center;
    justify-content: center;
    font-family: "Montserrat", sans-serif;
    font-weight: 600;
    font-size: 30px;
    letter-spacing: 9px;
    padding-left: 9px;
    box-sizing: border-box;
    color: var(--white);
  }
</style>
</head>
<body>
  <div class="cover">
    <svg class="cover-photo" viewBox="0 0 704 1120" preserveAspectRatio="none" role="img" aria-label="Foto: stiller See mit herbstlich gefärbtem Waldufer unter blauem Himmel mit Wolken, die sich im Wasser spiegeln">
      <defs>
        <linearGradient id="lake-scene" x1="0" y1="0" x2="0" y2="1">
          <stop offset="0" stop-color="#e9f3fb"/>
          <stop offset="0.35" stop-color="#a9d0ef"/>
          <stop offset="0.52" stop-color="#c9def0"/>
          <stop offset="0.57" stop-color="#9aa64a"/>
          <stop offset="0.66" stop-color="#7b8a3c"/>
          <stop offset="0.72" stop-color="#9bbad6"/>
          <stop offset="0.85" stop-color="#6f9ccc"/>
          <stop offset="1" stop-color="#315f96"/>
        </linearGradient>
      </defs>
      <rect width="704" height="1120" fill="url(#lake-scene)"/>
    </svg>
    <div class="title-glow"></div>

    <p class="author">Heike Sommerlund</p>
    <h1 class="title"><span>Die Hütte</span><span>im Moor</span></h1>
    <p class="subtitle">HOLDING ON</p>

    <div class="genre-tab">ROMAN</div>
  </div>
</body>
</html>
```